Oral Restoration Planners Guild Yearly Summit 2016 Flyer

We need a two page attention grabbing flyer promoting our upcoming conference in Dallas, TX at the Brindlewood Inn on August 27th and 28th 2016. The flyer should give information about the conference and what you will learn by attending and to accept registration through an Ticketvale link. Our mission is to define, educate and support the role of the dental implant coordinator. Bringing together like-minded professionals to network, practice share and define our role in the delivery of comprehensive patient care. 2 day annual conference open to Surgical implant coordinators and their surgeons

Target Market(s)

Surgical Implant Treatment Coordinators, their surgeons, and surgical team members

Industry/Entity Type

Dental

Requirements
Must have
• The ability for me to make changes.
Nice to have
• professional, eye catching,

```html
<!DOCTYPE html>
<html lang="en">
<head>
<meta charset="utf-8">
<title>Oral Restoration Planners Guild Yearly Summit 2016 Flyer</title>
<link rel="stylesheet" href="https://fonts.googleapis.com/css2?family=Roboto+Condensed:wght@700&family=Open+Sans:wght@400;600&display=swap">
<style>
  :root {
    --brand-blue: #1b7cc6;
    --brand-blue-deep: #0f66ad;
    --brand-grey: #5c5d60;
    --grey-light: #8a8b8e;
    --text-dark: #3a3a3c;
    --paper: #ffffff;
  }
  * { margin: 0; padding: 0; box-sizing: border-box; }
  html, body { width: 907px; height: 1200px; overflow: hidden; background: var(--paper); }
  .flyer { position: relative; width: 907px; height: 1200px; background: var(--paper); overflow: hidden; font-family: "Open Sans", Arial, sans-serif; }
  .flyer-art { position: absolute; inset: 0; }
  .brand { position: absolute; right: 38px; top: 46px; text-align: right; }
  .brand-mark { font-family: "Open Sans", Arial, sans-serif; font-weight: 400; font-size: 78px; line-height: 1; letter-spacing: 8px; color: var(--brand-blue); }
  .brand-name { font-family: "Open Sans", Arial, sans-serif; font-weight: 400; font-size: 15px; color: var(--text-dark); margin-top: 4px; }
  .condensed { font-family: "Roboto Condensed", "Arial Narrow", sans-serif; font-weight: 700; }
  .headline { position: absolute; left: 0; right: 0; top: 618px; text-align: center; font-size: 62px; line-height: 1; color: var(--brand-blue); letter-spacing: 0.5px; }
  .headline .year { color: var(--grey-light); }
  .date-pill { position: absolute; left: 59px; top: 705px; width: 796px; height: 99px; border-radius: 24px; background: linear-gradient(180deg, #838487 0%, #5b5c5f 100%); text-align: center; color: #fff; padding-top: 6px; }
  .date-pill .dates { font-size: 48px; line-height: 1.05; }
  .date-pill .venue { font-size: 28px; line-height: 1.3; }
  .mission { position: absolute; left: 40px; top: 834px; width: 560px; }
  .mission-title { font-size: 34px; color: var(--brand-blue); line-height: 1.1; }
  .mission-text { font-size: 16.5px; line-height: 1.33; color: var(--text-dark); margin-top: 8px; padding-left: 4px; }
  .audience { position: absolute; left: 41px; top: 992px; }
  .audience-lead { font-size: 28px; color: var(--brand-blue); line-height: 1.15; }
  .audience-rest { font-size: 25px; color: var(--brand-grey); line-height: 1.25; }
  .contact { position: absolute; right: 38px; top: 940px; text-align: right; color: #fff; }
  .contact-intro { font-size: 24px; line-height: 1.2; }
  .contact-call { font-size: 36px; line-height: 1.2; }
  .contact-phone { font-size: 43px; line-height: 1.25; letter-spacing: 0.5px; }
  .contact-line { font-family: "Open Sans", Arial, sans-serif; font-size: 19px; line-height: 1.75; display: flex; align-items: center; justify-content: flex-end; gap: 8px; }
  .contact-line svg { width: 18px; height: 18px; }
</style>
</head>
<body>
<main class="flyer">
  <svg class="flyer-art" viewBox="0 0 907 1200" width="907" height="1200" aria-hidden="false">
    <defs>
      <linearGradient id="speakerTone" x1="0" y1="0" x2="1" y2="1">
        <stop offset="0" stop-color="#d9d9d9"/>
        <stop offset="0.55" stop-color="#8f8f8f"/>
        <stop offset="1" stop-color="#3c3c3c"/>
      </linearGradient>
      <linearGradient id="familyTone" x1="0" y1="0" x2="1" y2="1">
        <stop offset="0" stop-color="#e8d2c0"/>
        <stop offset="0.5" stop-color="#d6ad8e"/>
        <stop offset="1" stop-color="#f1ece7"/>
      </linearGradient>
      <linearGradient id="cornerBlue" x1="0" y1="1" x2="1" y2="0">
        <stop offset="0" stop-color="#2a8fd9"/>
        <stop offset="1" stop-color="#0f66ad"/>
      </linearGradient>
    </defs>

    <path class="photo-speaker" role="img" aria-label="Black and white photo of a speaker at a laptop lectern addressing a conference audience"
          d="M350 150 H907 V518 Q650 560 380 532 Z" fill="url(#speakerTone)"/>
    <path d="M380 538 Q650 572 907 522 V542 Q650 596 380 556 Z" fill="var(--brand-blue)"/>
    <path d="M400 560 Q650 596 907 548 V556 Q650 608 400 568 Z" fill="var(--grey-light)"/>

    <path class="photo-family" role="img" aria-label="Photo of a smiling family of parents and two children"
          d="M0 112 Q300 62 468 140 Q560 250 482 400 Q420 500 300 522 L0 522 Z" fill="url(#familyTone)"/>
    <path d="M0 96 Q300 22 492 112 Q624 262 522 424 Q452 524 292 566" fill="none" stroke="var(--brand-blue)" stroke-width="38" stroke-linecap="round"/>
    <path d="M0 96 Q300 22 492 112" fill="none" stroke="#fff" stroke-width="5" transform="translate(0 -24)"/>
    <path d="M0 402 Q200 418 330 520" fill="none" stroke="var(--brand-blue)" stroke-width="22"/>
    <path d="M0 386 Q200 402 330 504" fill="none" stroke="#fff" stroke-width="4"/>

    <path d="M0 1080 Q240 1135 470 1108 L430 1200 H0 Z" fill="var(--brand-grey)"/>
    <path d="M0 1070 Q240 1125 470 1098" fill="none" stroke="#fff" stroke-width="4"/>

    <path d="M388 1200 Q590 928 907 818 V840 Q604 952 404 1200 Z" fill="var(--brand-grey)"/>
    <path d="M404 1200 Q604 952 907 840 V1200 Z" fill="url(#cornerBlue)"/>
  </svg>

  <header class="brand">
    <div class="brand-mark">ORPG</div>
    <div class="brand-name">Oral Restoration Planners Guild</div>
  </header>

  <h1 class="headline condensed">ANNUAL CONFERENCE <span class="year">2016</span></h1>

  <div class="date-pill">
    <div class="dates condensed">27th &amp; 28th August 2016</div>
    <div class="venue">in Dallas, TX at the Brindlewood Inn</div>
  </div>

  <section class="mission">
    <h2 class="mission-title condensed">Our mission</h2>
    <p class="mission-text">Educate and support the role of the dental implant coordinator. Bringing together like-minded professionals to network, practice share and define our role in the delivery of comprehensive patient care.</p>
  </section>

  <section class="audience condensed">
    <div class="audience-lead">2 day annual conference open</div>
    <div class="audience-rest">to Surgical implant coordinators<br>and their surgeons</div>
  </section>

  <section class="contact">
    <div class="contact-intro condensed">For more information</div>
    <div class="contact-call condensed">Call now</div>
    <div class="contact-phone condensed">0198765432</div>
    <div class="contact-line">www.contact@guildmail.com
      <svg viewBox="0 0 18 18"><rect x="1" y="4" width="16" height="11" rx="1" fill="#fff" opacity="0.8"/><path d="M1 4 L9 10 L17 4" fill="none" stroke="#1b7cc6" stroke-width="1.5"/></svg>
    </div>
    <div class="contact-line">www.guildsummit.com
      <svg viewBox="0 0 18 18"><circle cx="9" cy="9" r="7.5" fill="#fff" opacity="0.8"/><path d="M1.5 9 H16.5 M9 1.5 Q4 9 9 16.5 M9 1.5 Q14 9 9 16.5" fill="none" stroke="#1b7cc6" stroke-width="1.2"/></svg>
    </div>
  </section>
</main>
</body>
</html>
```